Jewelry Business card for general purpose. Elegant and simple

We are a jewelry group with 6 stores in Mexico and 30 years in business.

We need a BC that at leats includes the name, mail, phone number and physical location (street, municipality, and county; example "Paseo Olmeda 2140", "Avenida Sotillo", "Monterrey").
Optional: we are trying to reposition the brand with the association of life-events or moments and family. Such as: birth, marriage, graduation, birthdays. Christmast, mothers day and fathers day.

We are looking for something elegant but simple

Jewelry name: "Lunetti". Email: "lunettibrillo@correo-ejemplo.mx". Phone num "4172-3095".

Target Market(s)

General business card: from suppliers to clients. One segment outstand: couples gettineg married

Industry/Entity Type

Jewelry Store

Contact Information for Business Card

Loking for something simple but elegant.

Font styles to use
Decorative
Script

Requirements
Must have
• Must have name, address, and mail.
Nice to have
• It could have jewelry pictures/design. Maybe quotes. Or general words as background . currently we have a very simple card with one ring would like to see something different.
Should not have
• Include real people.

```html
<!DOCTYPE html>
<html lang="es">
<head>
<meta charset="utf-8">
<title>Lunetti – Tarjeta de presentación</title>
<link rel="stylesheet" href="https://fonts.googleapis.com/css2?family=Great+Vibes&family=Ubuntu:wght@400&display=swap">
<style>
  :root {
    --page: #ffffff;
    --pearl: #d9dcdd;
    --plum: #42004f;
    --plum-text: #3a0a4a;
    --logo: #7a1a9a;
    --white: #ffffff;
    --shadow: rgba(0, 0, 0, 0.35);
  }
  html, body {
    margin: 0;
    padding: 0;
    overflow: hidden;
    background: var(--page);
  }
  .canvas {
    position: relative;
    width: 974px;
    height: 1200px;
    overflow: hidden;
    background: var(--page);
  }
  .card {
    position: absolute;
    left: 65px;
    width: 836px;
    height: 462px;
    overflow: hidden;
    background: var(--pearl);
  }
  .card--front { top: 117px; }
  .card--back {
    top: 635px;
    background: var(--plum);
    box-shadow: 2px 3px 5px var(--shadow);
  }
  .card__shape {
    position: absolute;
    inset: 0;
    width: 100%;
    height: 100%;
  }
  .brand-name {
    position: absolute;
    left: 330px;
    top: 60px;
    margin: 0;
    font-family: "Great Vibes", cursive;
    font-weight: 400;
    font-size: 112px;
    line-height: 1;
    color: var(--logo);
  }
  .store-title {
    position: absolute;
    right: 40px;
    top: 60px;
    margin: 0;
    font-family: "Great Vibes", cursive;
    font-weight: 400;
    font-size: 62px;
    line-height: 1;
    color: var(--white);
  }
  .ring-photo {
    position: absolute;
    left: 535px;
    top: 185px;
    width: 225px;
    height: 210px;
    border-radius: 50%;
    background: radial-gradient(ellipse at 50% 40%, #f4f6fa 0%, #c4cad6 55%, rgba(160,168,185,0) 72%);
  }
  .contact {
    position: absolute;
    left: 44px;
    top: 272px;
    margin: 0;
    padding: 0;
    list-style: none;
    font-family: "Ubuntu", sans-serif;
    font-size: 20px;
    line-height: 28px;
    color: var(--plum-text);
  }
  .contact__item {
    display: flex;
    align-items: flex-start;
    margin-bottom: 25px;
  }
  .contact__item:first-child { margin-bottom: 27px; }
  .contact__icon {
    width: 24px;
    height: 24px;
    flex: none;
    margin-top: 2px;
    margin-right: 24px;
    fill: var(--plum-text);
  }
</style>
</head>
<body>
<main class="canvas">

  <section class="card card--front" aria-label="Frente de la tarjeta">
    <svg class="card__shape" viewBox="0 0 836 462" preserveAspectRatio="none" aria-hidden="true">
      <path d="M0 427 C 300 422 600 345 836 224 L836 462 L0 462 Z" fill="var(--plum)"/>
    </svg>
    <h1 class="brand-name">Lunetti</h1>
  </section>

  <section class="card card--back" aria-label="Reverso de la tarjeta">
    <svg class="card__shape" viewBox="0 0 836 462" preserveAspectRatio="none" aria-hidden="true">
      <path d="M0 104 C 260 110 610 235 836 452 L836 462 L0 462 Z" fill="var(--pearl)"/>
    </svg>
    <h2 class="store-title">Joyeria Lunetti</h2>
    <div class="ring-photo" role="img" aria-label="Fotografía de un anillo de compromiso con diamante"></div>

    <ul class="contact">
      <li class="contact__item">
        <svg class="contact__icon" viewBox="0 0 24 24" aria-hidden="true">
          <path d="M12 3 L1 13 H4 V21 H10 V15 H14 V21 H20 V13 H23 Z"/>
        </svg>
        <span>Paseo Olmeda 2140 ,<br>Avenida Sotillo, Monterrey</span>
      </li>
      <li class="contact__item">
        <svg class="contact__icon" viewBox="0 0 24 24" aria-hidden="true">
          <path d="M6.6 10.8a15.1 15.1 0 0 0 6.6 6.6l2.2-2.2c.3-.3.7-.4 1-.2 1.1.4 2.3.6 3.6.6.6 0 1 .4 1 1V20c0 .6-.4 1-1 1C10.6 21 3 13.4 3 4c0-.6.4-1 1-1h3.5c.6 0 1 .4 1 1 0 1.3.2 2.5.6 3.6.1.3 0 .7-.2 1z"/>
        </svg>
        <span>4172-3095</span>
      </li>
      <li class="contact__item">
        <svg class="contact__icon" viewBox="0 0 24 24" aria-hidden="true">
          <path d="M2 5 H22 V19 H2 Z M2 5 L12 13 L22 5" fill="var(--plum-text)" stroke="var(--pearl)" stroke-width="1.4" stroke-linejoin="round"/>
        </svg>
        <span>lunettibrillo@correo-ejemplo.mx</span>
      </li>
    </ul>
  </section>

</main>
</body>
</html>
```